KV HOLDINGS Business Cards

I need business cards for "KV Holdings group LLC" doublesided... logo on the back (also include logo on front)
logo attached to project... i have jpg up..
Company Info:
418 North Palmer Avenue, Suite 7B
Chicago, Illinois 60654
facsimile 312-555-0187 (list fax, address, website on all cards.)
www.kvholdingsgroup.example
Three different people on cards:
Darnell P. Okafor, CPA MST
Principal
ofc 312-555-0142
mobile 312-555-0169
darnellpokafor@kvholdingsgroup.example
Gregor T. Vanhoutte, CPA MST
Principal
gregortvanhoutte@kvholdingsgroup.example
mobile 708-555-0113
ofc 312-555-0142
Tobias M Quarrie
Principal
ofc 312-555-0142
no mobile
tobiasmquarrie@kvholdingsgroup.example
I have multiple projects listed.. see below:
Business cards for amber ledge partners llc
letterhead
envelopes
Business cards for KV Holdings LLC
letterhead
envelopes
Target Market(s)
rich people
Industry/Entity Type
Business

```html
<!DOCTYPE html>
<html lang="en">
<head>
<meta charset="utf-8">
<title>KV Holdings Group LLC – Business Cards</title>
<link rel="stylesheet" href="https://fonts.googleapis.com/css2?family=Tinos:wght@400;700&display=swap">
<style>
  :root {
    --backdrop: #d0d0d0;
    --card-white: #ffffff;
    --brand-blue: #05417a;
    --label-blue: #a9c0dc;
    --text-gray: #555555;
    --text-black: #111111;
    --text-white: #ffffff;
  }
  * { margin: 0; padding: 0; box-sizing: border-box; }
  html, body {
    width: 1200px; height: 1000px; overflow: hidden;
    background: var(--backdrop);
    font-family: "Tinos", "Times New Roman", serif;
  }
  .canvas { position: relative; width: 1200px; height: 1000px; }
  .card {
    position: absolute; width: 528px; height: 342px;
    background: var(--card-white);
    box-shadow: 4px 4px 5px rgba(0,0,0,0.45);
    text-align: center;
  }
  .card--gregor { left: 46px; top: 134px; }
  .card--tobias { left: 46px; top: 521px; }
  .card--darnell { left: 618px; top: 325px; }
  .person {
    position: absolute; left: 0; right: 0; top: 50px;
  }
  .person-name {
    font-size: 20px; font-weight: 700; color: var(--brand-blue);
    line-height: 26px;
  }
  .person-title {
    font-size: 15.5px; color: var(--text-gray); line-height: 22px;
  }
  .brand-mark {
    position: absolute; left: 0; right: 0; top: 124px;
    display: flex; justify-content: center; align-items: center; gap: 10px;
  }
  .brand-dot {
    width: 14px; height: 14px; border-radius: 50%;
    background: var(--brand-blue);
  }
  .brand-name {
    font-size: 22px; color: var(--brand-blue);
    font-variant: small-caps; letter-spacing: 0.5px; font-weight: 400;
  }
  .company-address {
    position: absolute; left: 0; right: 0; top: 158px;
    font-size: 15.5px; color: var(--text-gray);
  }
  .company-web {
    position: absolute; left: 0; right: 0; top: 181px;
    font-size: 16.5px; font-weight: 700; color: var(--text-black);
  }
  .contact-band {
    position: absolute; left: 0; right: 0; bottom: 0; height: 123px;
    background: var(--brand-blue);
    padding-top: 17px;
    font-size: 16px; line-height: 22px; color: var(--text-white);
  }
  .contact-band .label { font-weight: 700; color: var(--label-blue); }
</style>
</head>
<body>
<main class="canvas">

  <section class="card card--gregor">
    <div class="person">
      <p class="person-name">Gregor T. Vanhoutte, CPA MST</p>
      <p class="person-title">Principal</p>
    </div>
    <div class="brand-mark"><span class="brand-dot"></span><span class="brand-name">KV Holdings Group LLC</span></div>
    <p class="company-address">418 North Palmer Avenue, Suite 7B, Chicago, Illinois 60654</p>
    <p class="company-web">www.kvholdingsgroup.example</p>
    <div class="contact-band">
      <p><span class="label">office:</span> 312-555-0142</p>
      <p><span class="label">mobile:</span> 708-555-0113</p>
      <p><span class="label">facsimile:</span> 312-555-0187</p>
      <p>gregortvanhoutte@kvholdingsgroup.example</p>
    </div>
  </section>

  <section class="card card--tobias">
    <div class="person">
      <p class="person-name">Tobias M Quarrie</p>
      <p class="person-title">Principal</p>
    </div>
    <div class="brand-mark"><span class="brand-dot"></span><span class="brand-name">KV Holdings Group LLC</span></div>
    <p class="company-address">418 North Palmer Avenue, Suite 7B, Chicago, Illinois 60654</p>
    <p class="company-web">www.kvholdingsgroup.example</p>
    <div class="contact-band">
      <p><span class="label">office:</span> 312-555-0142</p>
      <p><span class="label">facsimile:</span> 312-555-0187</p>
      <p>tobiasmquarrie@kvholdingsgroup.example</p>
    </div>
  </section>

  <section class="card card--darnell">
    <div class="person">
      <p class="person-name">Darnell P. Okafor, CPA MST</p>
      <p class="person-title">Principal</p>
    </div>
    <div class="brand-mark"><span class="brand-dot"></span><span class="brand-name">KV Holdings Group LLC</span></div>
    <p class="company-address">418 North Palmer Avenue, Suite 7B, Chicago, Illinois 60654</p>
    <p class="company-web">www.kvholdingsgroup.example</p>
    <div class="contact-band">
      <p><span class="label">office:</span> 312-555-0142</p>
      <p><span class="label">mobile:</span> 312-555-0169</p>
      <p><span class="label">facsimile:</span> 312-555-0187</p>
      <p>darnellpokafor@kvholdingsgroup.example</p>
    </div>
  </section>

</main>
</body>
</html>
```